Small holiday retreat needs new Internet launch

"The Evolution from a Ruin into a Holiday Retreat.
My wife and I rebuilt a small farm in a remote village into a little holiday retreat. Though close to the Baltic Sea, we want to attract people with the desire to spend some days in a secluded place. Though remote it offers some luxury - and time ticks slower.
This summer was our third season and we want to adapt our Internet pages. Look at our business card - we want to keep this style.
It should be a bit mystic and should not attract the bargain hunter.
We realized that in summer our name "Wiesenlicht" (ie sunny hill) does not fit for the dark part of the year - then it is more like "Hollow Moor Gate".
We have a guesthouse (the former stable) and two tiny houses. Additionally, we have lavatory with sauna in the rebuilt barn and a fitness room.
On our farm live a few animals (dog, cats, chicken, bees) + wild visitors.
Our current home page is www.wiesenlicht-example.net
A few pictures are on Google Maps and I can share more in Google Drive.
The final homepage should also offer translations into English, French, Dutch.
Better and consistent fonts.
No "galery" but more "four seasons".

Target Market(s)

Individual travellers - not just from Germany!

Industry/Entity Type

Tourism

Coding

Coded - Design and coding required

Number of Pages Required

4 page

Font styles to use
Script

Colors
FFC000
F8CF3A
FAE287
FDF2CF
FEFAEE

Requirements
Must have
• A "mystic" and romantic appearance.
Nice to have
• See my comments.

```html
<!DOCTYPE html>
<html lang="de">
<head>
<meta charset="utf-8">
<title>Wiesenlicht – Reise in Deine Entspannung</title>
<link href="https://fonts.googleapis.com/css2?family=Great+Vibes&family=Poppins:wght@400;500;600;700&display=swap" rel="stylesheet">
<style>
:root{
  --gold:#FFC000;
  --gold-2:#F8CF3A;
  --gold-3:#FAE287;
  --cream:#FDF2CF;
  --ivory:#FEFAEE;
  --amber:#E89A00;
  --rust:#B86A00;
  --brown:#6E3E05;
  --night:#2E220F;
  --white:#ffffff;
  --ink:#3a2a12;
}
*{box-sizing:border-box;margin:0;padding:0}
html,body{width:1200px;height:3908px;overflow:hidden}
body{position:relative;font-family:"Poppins",sans-serif;color:var(--white);background:var(--amber)}
.abs{position:absolute}
.script{font-family:"Great Vibes",cursive;font-weight:400}

/* backgrounds */
.bg-page{left:0;top:0;width:1200px;height:3908px;background:linear-gradient(180deg,#d98a00 0%,#f0a800 30%,#f6b400 45%,#e39400 60%,#c97400 78%,#a55a00 88%)}
.hero-photo{left:0;top:0;width:1200px;height:800px;background:
  radial-gradient(ellipse at 20% 58%,rgba(40,70,30,.85),rgba(40,70,30,0) 22%),
  radial-gradient(ellipse at 85% 55%,rgba(35,65,25,.85),rgba(35,65,25,0) 20%),
  radial-gradient(ellipse at 50% 64%,rgba(230,230,220,.7),rgba(230,230,220,0) 8%),
  linear-gradient(180deg,#2f62c0 0%,#5f8fd6 25%,#a9c6e6 45%,#d7e4ec 53%,#4c7230 60%,#5c8a2e 75%,#7fae3e 100%)}
.reviews-photo{left:0;top:2050px;width:1200px;height:720px;background:radial-gradient(ellipse at 85% 40%,rgba(255,230,140,.8),rgba(230,150,20,0) 60%)}
.contact-photo{left:0;top:2770px;width:1200px;height:700px;background:linear-gradient(180deg,rgba(255,200,60,.2),rgba(140,70,0,.6)),radial-gradient(ellipse at 50% 30%,#ffd56a,#d47f00 70%)}

/* nav */
.nav{left:0;top:0;width:1200px;height:90px;display:flex;align-items:center;padding:0 40px}
.brand{display:flex;align-items:center;gap:10px;font-size:22px;font-weight:600;color:var(--white)}
.brand-dot{width:34px;height:34px;border-radius:50%;background:var(--gold)}
.menu{margin-left:150px;display:flex;gap:44px;font-size:12px;font-weight:600;letter-spacing:.5px}
.btn-contact{margin-left:50px;border:2px solid var(--white);border-radius:20px;padding:6px 18px;font-size:11px;font-weight:600}
.lang{margin-left:18px;width:24px;height:14px;background:linear-gradient(180deg,#233a8a 50%,#c8202a 50%)}

/* hero */
.hero-title{left:0;top:185px;width:1200px;text-align:center;font-size:84px;line-height:1.2;text-shadow:0 2px 6px rgba(0,0,0,.25)}
.hero-sub{left:0;top:295px;width:1200px;text-align:center;font-size:28px;font-weight:500;line-height:1.35;text-shadow:0 1px 4px rgba(0,0,0,.3)}
.btn-gold{background:var(--gold);color:var(--white);border-radius:30px;font-weight:600;font-size:14px;text-align:center}
.hero-btn{left:490px;top:392px;width:230px;height:54px;line-height:54px}

/* welcome */
.welcome-photo{left:170px;top:905px;width:350px;height:350px;border-radius:50%;border:10px solid var(--gold-2);background:
  radial-gradient(ellipse at 60% 55%,rgba(120,130,150,.9),rgba(120,130,150,0) 28%),
  linear-gradient(180deg,#e9895a 0%,#f3b27a 25%,#f7d2a0 48%,#8f9c6a 68%,#5e7a3a 100%);box-shadow:0 10px 30px rgba(80,40,0,.4)}
.welcome-title{left:560px;top:920px;width:560px;text-align:center;font-size:58px}
.welcome-text{left:590px;top:1015px;width:500px;text-align:center;font-size:15px;line-height:1.6}
.btn-outline{border:2px solid var(--white);border-radius:30px;font-size:13px;font-weight:600;text-align:center}
.welcome-btn{left:775px;top:1265px;width:150px;height:46px;line-height:42px}

/* domicile */
.section-title{left:0;width:1200px;text-align:center;font-size:64px}
.domicile-title{top:1430px;color:var(--gold-3)}
.card{top:1595px;width:250px;height:330px}
.card-photo{width:250px;height:180px}
.card-label{margin-top:16px;text-align:center;font-size:16px;font-weight:700;line-height:1.3}
.card-feature{top:1560px;left:345px;width:250px;height:380px;background:linear-gradient(180deg,#7a4306,#4f2a04);box-shadow:0 10px 30px rgba(60,30,0,.5)}
.card-feature .card-photo{height:200px}
.card-feature .card-label{margin-top:22px}
.card-feature p{font-size:11px;text-align:center;padding:8px 24px 0;line-height:1.5}
.btn-small{display:block;margin:14px auto 0;width:110px;height:34px;line-height:30px;font-size:11px}

/* reviews */
.reviews-title{top:2100px}
.review-photo{left:180px;top:2230px;width:440px;height:400px;background:
  radial-gradient(ellipse at 50% 60%,rgba(240,190,140,.9),rgba(240,190,140,0) 30%),
  radial-gradient(ellipse at 15% 80%,rgba(200,90,40,.9),rgba(200,90,40,0) 22%),
  linear-gradient(160deg,#7a3018 0%,#a9502a 30%,#c98556 55%,#e4c29a 80%,#f3e3c8 100%)}
.review-panel{left:600px;top:2230px;width:500px;height:400px}
.review-body{left:660px;top:2270px;width:400px;color:var(--ink)}
.review-lead{font-size:18px;font-weight:600;line-height:1.4;margin-bottom:14px;color:var(--brown)}
.review-text{font-size:13px;line-height:1.6}
.review-name{margin-top:16px;font-size:14px;font-weight:700;color:var(--brown)}
.arrow{top:2410px;width:30px;height:40px}

/* contact */
.contact-title{top:2720px}
.info{top:2840px;display:flex;align-items:center;gap:14px}
.info-icon{width:44px;height:44px;border-radius:50%;background:var(--white);display:flex;align-items:center;justify-content:center;flex:none}
.info small{display:block;font-size:12px}
.info strong{display:block;font-size:19px;font-weight:600}
.map{left:150px;top:2960px;width:500px;height:400px;background:
  radial-gradient(ellipse at 30% 30%,rgba(200,225,190,.9),rgba(200,225,190,0) 35%),
  radial-gradient(ellipse at 75% 75%,rgba(205,228,195,.8),rgba(205,228,195,0) 30%),
  linear-gradient(135deg,#eeece6,#dedcd4);border-radius:14px 0 0 14px}
.form{left:630px;top:2960px;width:420px;height:400px;background:var(--gold);border-radius:0 14px 14px 0;padding:40px 40px 0 40px}
.field{height:36px;border:1px solid rgba(255,255,255,.8);border-radius:4px;margin-bottom:12px;font-size:12px;line-height:34px;padding-left:36px}
.field.area{height:110px}
.btn-send{left:670px;top:3390px;width:150px;height:44px;line-height:44px;background:var(--night);border-radius:24px;font-size:12px;font-weight:600;text-align:center}

/* footer */
.footer{left:0;top:3480px;width:1200px;height:428px;background:var(--night)}
.foot-title{font-size:18px;font-weight:600;margin-bottom:18px}
.foot-col{top:3590px;font-size:14px;line-height:2.1}
.foot-contact{top:3640px;left:440px;font-size:13px;line-height:1.5}
.foot-contact div{display:flex;gap:12px;margin-bottom:14px}
.foot-contact span.ico{width:26px;height:26px;border-radius:5px;background:var(--gold);flex:none}
.news-input{width:270px;height:40px;background:var(--white);border-radius:4px;color:#777;font-size:12px;line-height:40px;padding-left:12px}
.news-btn{margin-top:14px;width:270px;height:40px;line-height:40px;background:var(--gold);border-radius:20px;text-align:center;font-size:13px;font-weight:600}
.socials{display:flex;gap:10px;margin-top:18px}
.socials span{width:26px;height:26px;border-radius:50%;background:var(--white)}
.copyright{left:0;top:3868px;width:1200px;text-align:center;font-size:12px;color:#d8c9a8}
</style>
</head>
<body>
<div class="abs bg-page"></div>
<div class="abs hero-photo" role="img" aria-label="Photo of a meadow with a tiny house and trees under a blue sky"></div>

<svg class="abs" style="left:0;top:560px" width="1200" height="320" viewBox="0 0 1200 320" aria-hidden="true">
  <path d="M0 180 C300 120 700 260 1200 110 L1200 320 L0 320Z" fill="#FAE287" opacity=".7"/>
  <path d="M0 210 C320 160 720 300 1200 150 L1200 320 L0 320Z" fill="#F8CF3A"/>
  <path d="M0 250 C350 200 760 320 1200 200 L1200 320 L0 320Z" fill="#e9a200"/>
</svg>

<nav class="abs nav">
  <div class="brand"><span class="brand-dot"></span>Wiesenlicht</div>
  <div class="menu"><span>ÜBER UNS</span><span>UNTERKÜNFTE</span><span>BUCHUNGEN &amp; KALENDER</span><span>GALERIE</span></div>
  <div class="btn-contact">CONTACT</div>
  <div class="lang"></div>
</nav>

<h1 class="abs hero-title script">Reise in Deine Entspannung</h1>
<p class="abs hero-sub">Herzlich willkommen auf dem Wiesenlicht<br>im schönen Heideland.</p>
<div class="abs btn-gold hero-btn">BOOK RETREAT</div>

<div class="abs welcome-photo" role="img" aria-label="Photo of a wooden tiny house on wheels at sunset"></div>
<h2 class="abs welcome-title script">Welcome to Our Website</h2>
<p class="abs welcome-text">Herzlich willkommen auf dem Wiesenlicht im schönen Heideland. Mit viel Liebe zum Detail haben wir unseren alten Resthof zu einem Ort der Erholung und des Entspannens gemacht. Egal ob im Tinyhouse "Sonnenblume" oder den Ferienwohnungen "Abendrot" und "Morgentau", in all unseren Unterkünften legen wir Wert darauf, dass Du Dich als Gast sofort wohlfühlst und Dich inmitten eines verwunschenen Gartens entspannst. Ruhig und idyllisch gelegen erreichst Du trotzdem schnell die Hafenstadt und die Seestadt sowie die Strände Dünenbucht, Haffwiese und Strandort.</p>
<div class="abs btn-outline welcome-btn">LEARN MORE</div>

<svg class="abs" style="left:0;top:1360px" width="1200" height="700" viewBox="0 0 1200 700" aria-hidden="true">
  <path d="M0 60 C400 0 800 120 1200 40 L1200 640 C800 700 400 600 0 660Z" fill="#F8CF3A" opacity=".55"/>
  <path d="M0 100 C420 40 820 150 1200 80 L1200 600 C820 660 420 560 0 620Z" fill="#e9a000" opacity=".5"/>
</svg>
<h2 class="abs section-title domicile-title script">Your Domicile</h2>

<div class="abs card" style="left:90px">
  <div class="card-photo" role="img" aria-label="Photo of the guesthouse Abendrot in the garden" style="background:radial-gradient(ellipse at 40% 65%,rgba(190,130,80,.9),rgba(190,130,80,0) 30%),linear-gradient(180deg,#6f9ad6,#a9c4e0 35%,#6d8f3e 60%,#4f6e2a)"></div>
  <div class="card-label">DESIGN REFUGE<br>"ABENDROT"</div>
</div>
<div class="abs card-feature">
  <div class="card-photo" role="img" aria-label="Photo of the bright interior of tiny house Sternchen" style="background:radial-gradient(ellipse at 50% 40%,rgba(255,245,220,.9),rgba(255,245,220,0) 35%),linear-gradient(180deg,#efe4cf,#cdb28a 60%,#8a6a44)"></div>
  <div class="card-label">TINY HOUSE<br>"STERNCHEN"</div>
  <p>Cozy nights under quiet stars, with garden views all round.</p>
  <div class="btn-outline btn-small">LEARN MORE</div>
</div>
<div class="abs card" style="left:610px">
  <div class="card-photo" role="img" aria-label="Photo of the bedroom in the Morgentau flat" style="background:radial-gradient(ellipse at 50% 70%,rgba(90,80,90,.8),rgba(90,80,90,0) 35%),linear-gradient(180deg,#e4ddd0,#a9977c 60%,#6d5a44)"></div>
  <div class="card-label">DESIGN REFUGE<br>"MORGENTAU"</div>
</div>
<div class="abs card" style="left:870px">
  <div class="card-photo" role="img" aria-label="Photo of the tiny house Sonnenblume in a green meadow" style="background:radial-gradient(ellipse at 50% 55%,rgba(170,130,80,.85),rgba(170,130,80,0) 25%),linear-gradient(180deg,#8fb5e2,#c3d7e6 40%,#7a9a46)"></div>
  <div class="card-label">TINY HOUSE<br>"SONNENBLUME"</div>
</div>

<div class="abs reviews-photo" role="img" aria-label="Soft sunset light over the fields"></div>
<h2 class="abs section-title reviews-title script">Customer Reviews</h2>
<div class="abs review-photo" role="img" aria-label="Photo of a smiling guest holding a mug next to a brick wall and candles"></div>
<svg class="abs review-panel" viewBox="0 0 500 400" aria-hidden="true">
  <path d="M60 0 H500 V400 H0 C80 300 -20 120 60 0Z" fill="#FAE287"/>
  <path d="M40 0 C-30 120 70 300 -10 400" stroke="#ffffff" stroke-width="6" fill="none"/>
</svg>
<div class="abs review-body">
  <p class="review-lead">A quiet garden and warm hosts made our stay truly restful and special.</p>
  <p class="review-text">We came for two nights and stayed five. The tiny house was spotless, the sauna was a treat after long walks and the mornings were slow and golden. Every small detail felt chosen with care. We are already planning our return next autumn season.</p>
  <p class="review-name">MARLA K.</p>
</div>
<svg class="abs arrow" style="left:130px" viewBox="0 0 30 40" aria-hidden="true"><path d="M22 4 L8 20 L22 36" stroke="#fff" stroke-width="4" fill="none"/></svg>
<svg class="abs arrow" style="left:1105px" viewBox="0 0 30 40" aria-hidden="true"><path d="M8 4 L22 20 L8 36" stroke="#fff" stroke-width="4" fill="none"/></svg>

<div class="abs contact-photo" role="img" aria-label="Golden sunset over the countryside"></div>
<h2 class="abs section-title contact-title script">Contact us</h2>
<div class="abs info" style="left:150px">
  <div class="info-icon"><svg width="22" height="22" viewBox="0 0 24 24"><path d="M6.6 10.8a15 15 0 0 0 6.6 6.6l2.2-2.2a1 1 0 0 1 1-.25 11 11 0 0 0 3.6.6 1 1 0 0 1 1 1V20a1 1 0 0 1-1 1A17 17 0 0 1 3 4a1 1 0 0 1 1-1h3.5a1 1 0 0 1 1 1c0 1.25.2 2.45.6 3.6a1 1 0 0 1-.25 1z" fill="#B86A00"/></svg></div>
  <div><small>Phone Number</small><strong>+49 150 000 111 22</strong></div>
</div>
<div class="abs info" style="left:450px">
  <div class="info-icon"><svg width="22" height="22" viewBox="0 0 24 24"><rect x="3" y="5" width="18" height="14" rx="2" fill="none" stroke="#B86A00" stroke-width="2"/><path d="M3 7l9 6 9-6" fill="none" stroke="#B86A00" stroke-width="2"/></svg></div>
  <div><small>Write Email us</small><strong>post@wiesenlicht-example.net</strong></div>
</div>
<div class="abs info" style="left:820px">
  <div class="info-icon"><svg width="22" height="22" viewBox="0 0 24 24"><path d="M12 2a7 7 0 0 0-7 7c0 5 7 13 7 13s7-8 7-13a7 7 0 0 0-7-7zm0 9.5A2.5 2.5 0 1 1 12 6.5a2.5 2.5 0 0 1 0 5z" fill="#B86A00"/></svg></div>
  <div><small>Address</small><strong style="font-size:16px;line-height:1.3">Stiller Pfad 7, 18000<br>Neudorf, Germany</strong></div>
</div>
<div class="abs map" role="img" aria-label="Map showing the location of the retreat"></div>
<div class="abs form">
  <div class="field">First Name</div>
  <div class="field">Phone Number</div>
  <div class="field">Email Address</div>
  <div class="field area">Message</div>
</div>
<div class="abs btn-send">SEND MESSAGE</div>

<svg class="abs" style="left:0;top:3420px" width="1200" height="80" viewBox="0 0 1200 80" aria-hidden="true"><path d="M0 40 C300 0 800 80 1200 30 L1200 80 L0 80Z" fill="#2E220F"/></svg>
<div class="abs footer"></div>
<div class="abs foot-col" style="left:150px"><div class="foot-title">Quick Links</div>About<br>Accommodation<br>Booking Calendar</div>
<div class="abs foot-col" style="left:310px;top:3634px">Our Gallery<br>Sitemap<br>Contact</div>
<div class="abs foot-contact">
  <div><span class="ico"></span>Stiller Pfad 7, 18000 Neudorf,<br>Germany</div>
  <div><span class="ico"></span>post@wiesenlicht-example.net</div>
  <div><span class="ico"></span>+49 150 000 111 22</div>
</div>
<div class="abs foot-col" style="left:800px;line-height:1.4">
  <div class="foot-title">Sign Up Newsletter</div>
  <div class="news-input">Email address</div>
  <div class="news-btn">SUBSCRIBE</div>
  <div class="socials"><span></span><span></span><span></span><span></span></div>
</div>
<p class="abs copyright">Copyright 2020 Wiesenlicht | Privacy Policy | Terms of Use</p>
</body>
</html>
```